**** Web design project for VornaSoft ****

For my ICT company VornaSoft I need a website.

We design, build and host web-applications and we have our own CMS product. In the references part we want to show sample websites (thumbnails) + links.

It should look modern (WEB 2.0), rounded corners.

I want the following menu' s:
- Home
- Services
- References
- News
- About VornaSoft
- Contact

Sample websites:
See attachments
http://www.plumvest.com
http://www.gadomirbureauwerk.nl

Reason: Want to take some time for feedback and improvements.

Reason: I'm waiting for a black background, with shadow and ambient light. You'll make a good chance!

Industry/Entity Type

It Company

Requirements
Must have
• - Fixed width (1024px), should fit on an IPad2
- Language selection English/Dutch
- Twitter/Facebook/LinkedIn/RSS icons
- Footer for Terms of use and Copyrights
- Search box
- 3 (or more) boxes for information i.e. news, blog or advertisements
Nice to have
• - Footer Site Map
- Contrasting background outside borders
- wide image (rotator) (with transperant sentence block)
- Shadow

```html
<!DOCTYPE html>
<html lang="en">
<head>
<meta charset="utf-8">
<title>VornaSoft – Home</title>
<link href="https://fonts.googleapis.com/css2?family=Titillium+Web:wght@400;600;700&display=swap" rel="stylesheet">
<style>
:root{
  --blue:#2566a3;
  --blue-dark:#1d5389;
  --blue-link:#2a6aa8;
  --link-light:#6cc3f5;
  --page:#f1f1f1;
  --panel:#f7f8fa;
  --border:#c8cacc;
  --text:#555a5f;
  --heading:#3c4146;
  --footer:#d7dfe2;
  --logo-grey:#5b6c78;
}
*{box-sizing:border-box;margin:0;padding:0}
html,body{width:1000px;height:1200px;overflow:hidden}
body{background:var(--page);font-family:"Titillium Web",Arial,sans-serif;color:var(--text);position:relative}
.abs{position:absolute}

/* top bar */
.topbar{left:11px;top:0;width:978px;height:41px;background:var(--blue)}
.lang-label{left:557px;top:13px;font:600 9.5px Arial,sans-serif;color:#fff;letter-spacing:.2px}
.flag{top:15px;width:18px;height:10px;border:1px solid #fff}
.flag-en{left:663px;background:repeating-linear-gradient(#c33 0 1.4px,#fff 1.4px 2.8px)}
.flag-en::before{content:"";position:absolute;left:0;top:0;width:8px;height:5px;background:#3b4f8f}
.flag-nl{left:689px;background:linear-gradient(#c33 0 33%,#fff 33% 66%,#2a4a94 66%)}
.flag-sep{left:685px;top:13px;width:1px;height:14px;background:#9dbbd9}
.search{left:744px;top:9px;width:149px;height:24px;background:#fff;border:1px solid #9ab;border-radius:3px 0 0 3px;font-size:12px;color:#888;padding:3px 10px}
.find{left:892px;top:9px;width:42px;height:24px;background:linear-gradient(#2f78bb,#1c5184);border:1px solid #164673;border-radius:0 3px 3px 0;color:#fff;font:600 9.5px Arial,sans-serif;text-align:center;line-height:22px}

/* header */
.brand{left:14px;top:60px;display:flex;align-items:center;gap:16px}
.brand-dot{width:62px;height:62px;border-radius:50%;background:#2d8fd6}
.brand-name{font-size:31px;font-weight:400;color:var(--logo-grey);letter-spacing:.5px}
.social{left:820px;top:78px;width:107px;height:33px;border:1px solid #cfd4d8;border-radius:4px;background:#f8f9fa;display:flex;gap:7px;padding:8px 9px}
.social span{width:16px;height:16px;border-radius:2px}

/* nav */
.nav{left:11px;top:151px;width:978px;height:52px;border:1px solid #bdbdbd;border-radius:4px 4px 0 0;background:linear-gradient(#f3f3f3,#c9c9c9);overflow:hidden}
.nav ul{list-style:none;display:flex;height:100%}
.nav li{height:100%;border-right:1px solid #b5b5b5;border-left:1px solid #eee;text-align:center;font-size:14px;color:var(--blue-link);line-height:46px;position:relative}
.nav li::after{content:"";position:absolute;left:0;right:0;bottom:0;height:5px;background:#8e8e8e}
.nav li.active{background:linear-gradient(#dedede,#c4c4c4)}
.nav li.active::after{background:#2f7fcf}

/* hero */
.hero{left:11px;top:204px;width:978px;height:315px;border-radius:0 0 4px 4px;overflow:hidden;box-shadow:0 8px 10px -6px rgba(0,0,0,.35)}
.hero-visual{left:0;top:0;width:767px;height:315px;background:radial-gradient(ellipse at 60% 55%,#c9cbc6 0 14%,#4d6862 34%,#1f3430 70%,#0f1a18)}
.caption{left:0;top:254px;width:685px;height:61px;background:rgba(40,44,46,.82);padding:4px 24px;color:#fff}
.caption h1{font-size:21px;font-weight:400}
.caption h1 b{font-weight:700}
.caption p{font-size:12px;color:#dde;margin-top:-3px}
.caption-more{left:685px;top:254px;width:82px;height:61px;background:var(--blue);color:#fff;font-size:12px;font-weight:600;text-align:center;line-height:61px}
.news-col{left:767px;top:0;width:211px;height:315px;background:var(--blue)}
.news-item{height:105px;padding:10px 8px;border-bottom:1px solid #4b84ba;color:#fff}
.news-item h3{font-size:14px;font-weight:600}
.news-item p{font-size:12px;line-height:18px}
.news-item a{font-size:11.5px;font-weight:600;color:var(--link-light);text-decoration:none}

/* main panel */
.panel{left:11px;top:549px;width:978px;height:585px;background:var(--panel);border:1px solid var(--border);border-radius:4px;overflow:hidden}
.feature{top:18px;width:300px}
.feature svg{position:absolute;left:0;top:2px}
.feature h2{margin-left:42px;font-size:18.5px;font-weight:600;color:var(--blue)}
.feature p{margin-left:43px;margin-top:2px;font-size:12.6px;line-height:20px;width:246px}
.btn{display:block;margin:17px 0 0 43px;width:100px;height:28px;background:var(--blue);border:1px solid var(--blue-dark);color:#fff;font-size:12px;text-align:center;line-height:26px}
.clients-rule{left:0;top:239px;width:978px;height:1px;background:#cfd2d4}
.clients-title{left:0;top:227px;width:978px;text-align:center}
.clients-title span{background:var(--panel);padding:0 8px;font-size:18px;font-weight:600;color:var(--heading)}
.clients-text{left:38px;top:262px;width:902px;text-align:center;font-size:12.5px;line-height:20px}
.clients-strip{left:178px;top:365px;width:622px;height:41px;background:#fff;display:flex;justify-content:space-around;align-items:center;font-size:16px;font-weight:700;color:#8e8e8e}
.footer{left:0;top:462px;width:978px;height:123px;background:var(--footer);border-top:1px solid #cfd6d9}
.fcol{top:16px;font-size:9.5px;line-height:12px;color:#404548}
.fcol h4{font-size:9.5px;font-weight:700;color:var(--blue);padding-bottom:4px;border-bottom:1px solid #b9c5ca;margin-bottom:6px}
.fcol ul{list-style:none}
.fbrand{left:764px;top:24px;display:flex;align-items:center;gap:10px}
.fbrand .brand-dot{width:56px;height:56px;background:#7c8489}
.fbrand .brand-name{font-size:27px;color:#6c7479}
.copyright{left:0;top:1151px;width:1000px;text-align:center;font-size:12px;color:var(--blue)}
</style>
</head>
<body>
<header>
  <div class="abs topbar"></div>
  <div class="abs lang-label">CHOOSE LANGUAGE:</div>
  <span class="abs flag flag-en" aria-label="English"></span>
  <span class="abs flag-sep"></span>
  <span class="abs flag flag-nl" aria-label="Nederlands"></span>
  <div class="abs search">Search</div>
  <div class="abs find">FIND</div>

  <div class="abs brand"><span class="brand-dot"></span><span class="brand-name">VornaSoft</span></div>
  <div class="abs social" aria-label="Social links">
    <span style="background:#3b5a9a"></span><span style="background:#39a6d6"></span><span style="background:#1c7ab4"></span><span style="background:#f08a1c"></span>
  </div>

  <nav class="abs nav">
    <ul>
      <li class="active" style="width:117px">Home</li>
      <li style="width:167px">Services</li>
      <li style="width:186px">References</li>
      <li style="width:152px">News</li>
      <li style="width:212px">About VornaSoft</li>
      <li style="flex:1">Contact</li>
    </ul>
  </nav>
</header>

<section class="abs hero">
  <div class="abs hero-visual" role="img" aria-label="Photo of a white computer mouse and keyboard on a desk in front of a monitor"></div>
  <div class="abs caption"><h1>Hi, Welcome to <b>VornaSoft</b></h1><p>Lorem ipsum dolor sit amet, consectetur adipisicing elit, sed do eiusmod tempor incididunt ut labore et dolore magna aliqua.</p></div>
  <div class="abs caption-more">Read More</div>
  <div class="abs news-col">
    <div class="news-item"><h3>Very Long News Title Here</h3><p>Lorem ipsum dolor sit amet, con-sectetur adipisicing elit, sed do et.</p><a href="#">Read more &gt;&gt;</a></div>
    <div class="news-item"><h3>Second News Title Here</h3><p>Lorem ipsum dolor sit amet, con-sectetur adipisicing elit, sed do et.</p><a href="#">Read more &gt;&gt;</a></div>
    <div class="news-item" style="border:0"><h3>Very Long News Title Here</h3><p>Lorem ipsum dolor sit amet, con-sectetur adipisicing elit, sed do et.</p><a href="#">Read more &gt;&gt;</a></div>
  </div>
</section>

<main class="abs panel">
  <article class="abs feature" style="left:19px">
    <svg width="26" height="22" viewBox="0 0 26 22"><rect x="9" y="1" width="8" height="5" rx="1" fill="none" stroke="#333" stroke-width="2"/><rect x="1" y="5" width="24" height="15" rx="2" fill="#333"/><rect x="1" y="11" width="24" height="1.5" fill="#fff"/></svg>
    <h2>Our Services</h2>
    <p>Lorem ipsum dolor sit amet, consectetur adipisicing elit, sed do eiusmod tempor incidid-unt ut labore et dolore magna aliqua. Ut enim ad minim veniam, quis nostrud exercitation ullamco laboris nisi ut aliquip ex ea commodo.</p>
    <span class="btn">Read More</span>
  </article>
  <article class="abs feature" style="left:336px">
    <svg width="28" height="28" viewBox="0 0 28 28"><circle cx="14" cy="14" r="12" fill="none" stroke="#333" stroke-width="2.2"/><path d="M14 14 L9 8" stroke="#333" stroke-width="2.2"/><circle cx="14" cy="14" r="2" fill="#333"/></svg>
    <h2>About VornaSoft</h2>
    <p>Lorem ipsum dolor sit amet, consectetur adipisicing elit, sed do eiusmod tempor incidid-unt ut labore et dolore magna aliqua. Ut enim ad minim veniam, quis nostrud exercitation ullamco laboris nisi ut aliquip ex ea commodo.</p>
    <span class="btn">Read More</span>
  </article>
  <article class="abs feature" style="left:673px">
    <svg width="30" height="30" viewBox="0 0 30 30"><circle cx="11" cy="11" r="7" fill="none" stroke="#333" stroke-width="4" stroke-dasharray="3 2.5"/><circle cx="11" cy="11" r="4" fill="#333"/><circle cx="23" cy="23" r="4" fill="none" stroke="#333" stroke-width="3" stroke-dasharray="2 1.6"/></svg>
    <h2>Our References</h2>
    <p>Lorem ipsum dolor sit amet, consectetur adipisicing elit, sed do eiusmod tempor incidid-unt ut labore et dolore magna aliqua. Ut enim ad minim veniam, quis nostrud exercitation ullamco laboris nisi ut aliquip ex ea commodo.</p>
    <span class="btn">Read More</span>
  </article>

  <div class="abs clients-rule"></div>
  <div class="abs clients-title"><span>Our Clients</span></div>
  <p class="abs clients-text">Lorem ipsum dolor sit amet, consectetur adipisicing elit, sed do eiusmod tempor incididunt ut labore et dolore magna aliqua. Ut enim ad minim veniam, quis nostrud exercitation ullamco laboris nisi ut aliquip ex ea commodo consequat.Lorem ipsum dolor sit amet, consectetur adipisicing elit, sed do eiusmod tempor incididunt ut labore et dolore magna aliqua. Ut enim ad minim veniam, quis nostrud exercitation ullamco laboris nisi ut aliquip ex ea commodo consequat.</p>
  <div class="abs clients-strip"><span>Harbor Ledger</span><span>ByteQuarry</span><span>Lumenfeed</span><span>Northlane Web</span></div>

  <footer class="abs footer">
    <div class="abs fcol" style="left:19px;width:114px"><h4>ABOUT US</h4><ul><li>About Us</li><li>The VornaSoft Difference</li><li>Customers &amp; Testimonials</li><li>Awards</li><li>Events</li></ul></div>
    <div class="abs fcol" style="left:157px;width:114px"><h4>REFERENCES</h4><ul><li>Reference 1</li><li>Another Reference</li><li>Unique Reference here</li></ul></div>
    <div class="abs fcol" style="left:295px;width:204px"><h4>SERVICES</h4>
      <ul style="float:left;width:114px"><li>Application</li><li>Designing</li><li>User Interface</li><li>UX</li><li>Services widget</li></ul>
      <ul style="float:left"><li>Application</li><li>Designing</li><li>User Interface</li><li>UX</li></ul></div>
    <div class="abs fcol" style="left:522px;width:114px"><h4>NEWS</h4><ul><li>News Title Here</li><li>News Title Here</li><li>News Title Here</li><li>News Title Here</li><li>News Title Here</li></ul></div>
    <div class="abs fbrand"><span class="brand-dot"></span><span class="brand-name">VornaSoft</span></div>
  </footer>
</main>

<p class="abs copyright">Copyright © 2012 VornaSoft. All rights reserved.</p>
</body>
</html>
```